3D Buchcover für ebook
Das Design kam überraschend und war quasi aus dem Stand perfekt. Ich konnte gar nicht anders, als es zum Gewinner zu küren.
Zielgruppe
Das Buch erscheint als ebook, später auch als gedruckte Version. Es spricht Personen an, die mittels einer Diät nicht nur ihre Figur, sondern auch ihre Gesundheit, Fitneß und das Aussehen im Allgemeinen verbessern wollen. Die Hauptzielgruppe sind Frauen zwischen 35 und 60+.
Branche: Medizin/Gesundheit.
Aufgabenstellung
Hergestellt werde soll das Cover für ein ebook mit dem Titel "Der schmale Gürtel als klarer Beweis". Außerdem soll folgende Headline untegebracht werden: "Rückblick auf 13 Jahre Alltag ohne Zucker". Es soll ein Bild der Autorin verwendet werden. Aus den gelieferten Vorlagen kann die Frauenfigur ausgeschnitten werden. Wichtig ist, ihre Figur und die Ausstrahlung wirkungsvoll zur Geltung zu bringen. Unter den mitgelieferten Deteien ist außerdem das aktuelle Cover enthalten (das Buch ist bereits veröffentlicht). Auch der Autorname "Hanna Lübeck" soll auf dem Cover Platz finden.
Das Cover soll auch im Kleinformat, wie es üblicherweise in den Suchergebnissen auf Veltrix angezeigt wird, eine Aussagekraft besitzen.

```html
<!DOCTYPE html>
<html lang="de">
<head>
<meta charset="utf-8">
<title>Der schmale Gürtel als klarer Beweis – Cover</title>
<link rel="stylesheet" href="https://fonts.googleapis.com/css2?family=Bebas+Neue&family=Parisienne&family=Sacramento&display=swap">
<style>
  :root {
    --page: #ffffff;
    --denim-light: #6f8aaa;
    --denim-mid: #4a6587;
    --denim-deep: #1f3156;
    --portrait-warm: #b98a6a;
    --portrait-top: #1b2246;
    --portrait-jeans: #2c4a86;
    --title-white: #ffffff;
    --title-red: #ee1c25;
    --label-paper: #d8cdb4;
    --label-ink: #1f2a5c;
    --rivet: #a08a5e;
    --link-blue: #0066c0;
    --price-red: #b12704;
    --muted: #666666;
    --accent-orange: #e47911;
  }
  * { box-sizing: border-box; margin: 0; padding: 0; }
  html, body { width: 1200px; height: 1087px; overflow: hidden; background: var(--page); }
  .board { position: relative; width: 1200px; height: 1087px; overflow: hidden; }

  .cover { position: absolute; width: 766px; height: 1087px; overflow: hidden; transform-origin: 0 0; }
  .cover-denim {
    position: absolute; inset: 0;
    background: linear-gradient(180deg, var(--denim-light) 0%, var(--denim-mid) 50%, var(--denim-deep) 100%);
  }
  .author-photo {
    position: absolute; left: 395px; top: 62px; width: 371px; height: 1025px;
    border-radius: 170px 0 0 0;
    background: linear-gradient(180deg, var(--portrait-warm) 0%, var(--portrait-warm) 28%, var(--portrait-top) 40%, var(--portrait-top) 62%, var(--portrait-jeans) 78%, var(--denim-deep) 100%);
  }
  .author-label {
    position: absolute; left: 147px; top: 156px; width: 228px; height: 86px;
    background: var(--label-paper); transform: rotate(4deg);
    font-family: "Sacramento", cursive; font-size: 44px; line-height: 1; color: var(--label-ink);
    white-space: nowrap;
    display: flex; align-items: center; justify-content: center;
  }
  .rivet { position: absolute; left: 391px; top: 176px; width: 40px; height: 40px; border-radius: 50%; background: var(--rivet); }
  .cover-title {
    position: absolute; left: 54px; top: 432px;
    font-family: "Bebas Neue", sans-serif; font-size: 150px; line-height: 128px;
    color: var(--title-white); text-shadow: 0 4px 14px rgba(0,0,0,.45);
    white-space: nowrap;
  }
  .cover-title .accent { color: var(--title-red); }
  .cover-subtitle {
    position: absolute; left: 54px; top: 988px; width: 700px;
    font-family: "Parisienne", cursive; font-size: 40px; color: var(--title-white);
    white-space: nowrap;
  }

  .listing {
    position: absolute; left: 810px; top: 383px; width: 400px; height: 199px;
    background: #fff; box-shadow: 3px 4px 6px rgba(0,0,0,.35);
    font-family: Arial, Helvetica, sans-serif;
  }
  .listing-thumb { position: absolute; left: 28px; top: 8px; width: 128px; height: 182px; overflow: hidden; }
  .listing-thumb .cover { transform: scale(.1671); }
  .listing-info { position: absolute; left: 201px; top: 18px; white-space: nowrap; }
  .listing-title { font-size: 16px; color: var(--link-blue); }
  .listing-author { font-size: 12px; color: var(--muted); margin-top: 4px; }
  .listing-format { font-size: 12px; color: var(--link-blue); margin-top: 16px; }
  .price { font-size: 13px; font-weight: bold; color: var(--price-red); margin-top: 3px; }
  .price .note { font-weight: normal; color: var(--muted); }
  .price .flat { font-weight: normal; color: var(--accent-orange); }
  .small { font-size: 11px; color: var(--muted); margin-top: 3px; }

  .thumb-large {
    position: absolute; left: 810px; top: 625px; width: 244px; height: 346px; overflow: hidden;
    box-shadow: 4px 5px 7px rgba(0,0,0,.45);
  }
  .thumb-large .cover { transform: scale(.3185); }
</style>
</head>
<body>
<main class="board">

  <section class="cover" style="left:0;top:0">
    <div class="cover-denim" role="img" aria-label="Großaufnahme einer Jeans-Gesäßtasche als Hintergrund"></div>
    <div class="author-photo" role="img" aria-label="Foto der Autorin mit lockigem Haar, dunklem Trägertop und Jeans, sitzend"></div>
    <div class="author-label">Hanna Lübeck</div>
    <div class="rivet"></div>
    <h1 class="cover-title">DER <span class="accent">SCHMALE</span><br><span class="accent">GÜRTEL</span><br>ALS KLARER<br>BEWEIS</h1>
    <p class="cover-subtitle">Rückblick auf 13 Jahre Alltag ohne Zucker</p>
  </section>

  <article class="listing">
    <div class="listing-thumb">
      <div class="cover">
        <div class="cover-denim" role="img" aria-label="Jeans-Hintergrund"></div>
        <div class="author-photo" role="img" aria-label="Foto der Autorin in Jeans"></div>
        <div class="author-label">Hanna Lübeck</div>
        <div class="rivet"></div>
        <div class="cover-title">DER <span class="accent">SCHMALE</span><br><span class="accent">GÜRTEL</span><br>ALS KLARER<br>BEWEIS</div>
        <p class="cover-subtitle">Rückblick auf 13 Jahre Alltag ohne Zucker</p>
      </div>
    </div>
    <div class="listing-info">
      <div class="listing-title">Der schmale Gürtel als klarer Beweis</div>
      <div class="listing-author">von Hanna Lübeck</div>
      <div class="listing-format">Folio Edition</div>
      <div class="price">EUR 0,00 <span class="flat">folioflat</span></div>
      <div class="small">Abonnenten lesen kostenlos. Weitere</div>
      <div class="price" style="margin-top:10px">EUR 0,89 <span class="note">kaufen</span></div>
      <div class="small">Jetzt als Download verfügbar.</div>
    </div>
  </article>

  <div class="thumb-large">
    <div class="cover">
      <div class="cover-denim" role="img" aria-label="Jeans-Hintergrund"></div>
      <div class="author-photo" role="img" aria-label="Foto der Autorin in Jeans"></div>
      <div class="author-label">Hanna Lübeck</div>
      <div class="rivet"></div>
      <div class="cover-title">DER <span class="accent">SCHMALE</span><br><span class="accent">GÜRTEL</span><br>ALS KLARER<br>BEWEIS</div>
      <p class="cover-subtitle">Rückblick auf 13 Jahre Alltag ohne Zucker</p>
    </div>
  </div>

</main>
</body>
</html>
```